Home Baker of cakes, muffins, cookies and pastries.

I am looking for business cards for my home baking business called " Zippy Pom-Pom Bakes " - I want them to be super cute and girly, yet simple and modern at the same time. Pastel colours is what I envision with the main colour being baby pink.

```html
<!DOCTYPE html>
<html lang="en">
<head>
<meta charset="utf-8">
<title>Zippy Pom-Pom Bakes – Business Card</title>
<link href="https://fonts.googleapis.com/css2?family=Cookie&family=Work+Sans:wght@400;500&display=swap" rel="stylesheet">
<style>
  :root {
    --backdrop: #1d1c1d;
    --baby-pink: #f4aec5;
    --pink-soft: #f8cbd9;
    --pink-deep: #ec8fb0;
    --pink-back-light: #f2b1c7;
    --pink-back-dark: #d68ea5;
    --card-white: #ffffff;
    --ink: #4a4a4a;
  }
  html, body {
    margin: 0;
    padding: 0;
    width: 1200px;
    height: 963px;
    overflow: hidden;
    background: var(--backdrop);
  }
  .canvas {
    position: relative;
    width: 1200px;
    height: 963px;
    display: flex;
    align-items: center;
    justify-content: center;
    gap: 40px;
  }
  .card {
    position: relative;
    width: 520px;
    height: 298px;
    border-radius: 16px;
    overflow: hidden;
    box-shadow: 0 12px 30px rgba(0,0,0,0.5);
  }
  .card-front { background: var(--card-white); }
  .card-front .wave {
    position: absolute;
    inset: 0;
    width: 100%;
    height: 100%;
  }
  .brand-name {
    position: absolute;
    left: 32px;
    top: 58px;
    margin: 0;
    font-family: 'Cookie', cursive;
    font-weight: 400;
    font-size: 30px;
    color: var(--pink-deep);
    line-height: 1;
    white-space: nowrap;
  }
  .person {
    position: absolute;
    right: 40px;
    top: 166px;
    text-align: right;
  }
  .person-name {
    font-family: 'Cookie', cursive;
    font-size: 32px;
    color: var(--pink-deep);
    line-height: 1;
    margin: 0;
    white-space: nowrap;
  }
  .person-role {
    font-family: 'Work Sans', sans-serif;
    font-size: 12px;
    color: var(--ink);
    margin: 0;
  }
  .divider {
    position: absolute;
    left: 32px;
    right: 40px;
    top: 224px;
    height: 1px;
    background: var(--pink-deep);
  }
  .contact-list {
    position: absolute;
    left: 32px;
    top: 232px;
    margin: 0;
    padding: 0;
    list-style: none;
    font-family: 'Work Sans', sans-serif;
    font-size: 11px;
    color: var(--ink);
  }
  .contact-list li {
    display: flex;
    align-items: center;
    gap: 8px;
    height: 18px;
  }
  .contact-list svg { width: 10px; height: 10px; flex: none; }
  .address {
    position: absolute;
    right: 40px;
    top: 234px;
    margin: 0;
    text-align: right;
    font-family: 'Work Sans', sans-serif;
    font-style: normal;
    font-size: 11px;
    line-height: 18px;
    color: var(--ink);
  }
  .card-back {
    background: radial-gradient(ellipse at 35% 55%, var(--pink-back-light) 0%, var(--pink-back-dark) 100%);
    display: flex;
    align-items: center;
    justify-content: center;
  }
  .back-brand {
    margin: 0;
    font-family: 'Cookie', cursive;
    font-weight: 400;
    font-size: 58px;
    color: #f4f0f2;
  }
</style>
</head>
<body>
<main class="canvas">
  <section class="card card-front">
    <svg class="wave" viewBox="0 0 520 298" preserveAspectRatio="none" aria-hidden="true">
      <path d="M170 0 C290 8 320 60 350 95 C385 135 440 152 520 158 L520 0 Z" fill="var(--pink-soft)"/>
      <path d="M190 0 C305 8 335 58 365 92 C400 130 450 146 520 151 L520 0 Z" fill="var(--card-white)"/>
      <path d="M200 0 C312 8 342 57 372 90 C407 128 455 142 520 146 L520 0 Z" fill="var(--pink-soft)"/>
      <path d="M225 0 C330 6 360 55 390 86 C422 120 465 134 520 138 L520 0 Z" fill="var(--baby-pink)"/>
    </svg>
    <h1 class="brand-name">Zippy Pom-Pom Bakes</h1>
    <div class="person">
      <p class="person-name">Daisy Harlow</p>
      <p class="person-role">Director</p>
    </div>
    <div class="divider"></div>
    <ul class="contact-list">
      <li>
        <svg viewBox="0 0 10 10"><path d="M2 1 L4 1 L4.6 3 L3.4 3.8 C4 5 5 6 6.2 6.6 L7 5.4 L9 6 L9 8 C5 9 1 5 2 1 Z" fill="var(--pink-deep)"/></svg>
        555-014-2276
      </li>
      <li>
        <svg viewBox="0 0 10 10"><rect x="1" y="2" width="8" height="6" fill="none" stroke="var(--pink-deep)"/><path d="M1 2 L5 5.5 L9 2" fill="none" stroke="var(--pink-deep)"/></svg>
        hello@zippypompom.com
      </li>
      <li>
        <svg viewBox="0 0 10 10"><circle cx="5" cy="5" r="4" fill="none" stroke="var(--pink-deep)"/><path d="M1 5 H9 M5 1 C3 3 3 7 5 9 C7 7 7 3 5 1" fill="none" stroke="var(--pink-deep)" stroke-width="0.8"/></svg>
        www.zippypompom.com
      </li>
    </ul>
    <address class="address">14 Maple Row,<br>Brookfield, Zimbabwe</address>
  </section>

  <section class="card card-back">
    <h2 class="back-brand">Zippy Pom-Pom Bakes</h2>
  </section>
</main>
</body>
</html>
```